Black Friday Sale - Banner

Black Friday Sale. for website
https://quenlodrift.com/
Our Black Friday sale includes a free product with a purchase of any flat iron.
banner size is 1880x720
Must include Black Friday Deal
Free Heat Protectant Spray with all purchases
Target Market(s)
Hair Care Professionals
Industry/Entity Type
Beauty Salon
Font styles to use
Sans Serif
Colors
86cae7
ec1f27
ffffff
Requirements
Must have
- Must have a photo image of the product that is free
Can include images of flat irons from website
Nice to have
- images from website
Should not have
- white person

```html
<!DOCTYPE html>
<html lang="en">
<head>
<meta charset="utf-8">
<title>Black Friday Deal Banner</title>
<link rel="stylesheet" href="https://fonts.googleapis.com/css2?family=Archivo+Black&family=Sacramento&display=swap">
<style>
  :root {
    --red: #ec1f27;
    --red-deep: #c4060b;
    --red-light: #e8262b;
    --sky: #86cae7;
    --sky-deep: #74b9d8;
    --steel: #6f96a6;
    --steel-deep: #5f8594;
    --white: #ffffff;
    --black: #050505;
    --photo-dark: #3a1f1a;
    --photo-warm: #c27a52;
    --page: #ffffff;
  }
  * { margin: 0; padding: 0; box-sizing: border-box; }
  html, body { width: 1200px; height: 1090px; overflow: hidden; background: var(--page); }
  .canvas { position: relative; width: 1200px; height: 1090px; }

  .banner {
    position: absolute; left: 56px; width: 1088px; height: 416px; overflow: hidden;
    background:
      radial-gradient(ellipse 420px 160px at 540px 40px, rgba(255,80,80,.35), transparent 70%),
      radial-gradient(ellipse 500px 200px at 900px 330px, rgba(120,0,0,.25), transparent 70%),
      linear-gradient(160deg, var(--red-deep) 0%, var(--red) 45%, var(--red-light) 60%, var(--red-deep) 100%);
    font-family: "Archivo Black", sans-serif;
  }
  .banner--first { top: 88px; }
  .banner--second { top: 636px; }

  .product {
    position: absolute; width: 193px; height: 193px; border-radius: 50%;
    border: 6px solid var(--white);
  }
  .product--set { left: 31px; top: 22px; background: linear-gradient(160deg, var(--sky) 0%, var(--sky-deep) 100%); }
  .product--spray { left: 128px; top: 202px; background: linear-gradient(160deg, var(--steel) 0%, var(--steel-deep) 100%); }

  .frame { position: absolute; left: 0; top: 0; }

  .title-black {
    position: absolute; left: 0; width: 1086px; top: 62px; text-align: center;
    font-size: 74px; line-height: 1; color: var(--white);
    text-shadow: 0 0 10px rgba(255,255,255,.7), 0 0 22px rgba(255,255,255,.45);
  }
  .title-friday {
    position: absolute; left: 0; width: 1086px; top: 132px; text-align: center;
    font-size: 90px; line-height: 1; color: var(--black); letter-spacing: -1px;
  }
  .title-deal {
    position: absolute; left: 0; width: 1086px; top: 184px; text-align: center;
    font-family: "Sacramento", cursive; font-size: 106px; line-height: 1; color: var(--white);
    padding-right: 6px;
  }
  .offer {
    position: absolute; left: 0; width: 1086px; top: 294px; text-align: center;
    font-size: 13px; line-height: 16px; color: var(--sky); letter-spacing: .6px;
  }
  .shop-now {
    position: absolute; left: 437px; top: 349px; width: 209px; height: 42px;
    border: 2px solid var(--white); color: var(--white);
    font-size: 20px; letter-spacing: 3px; text-align: center; line-height: 38px;
  }
  .model {
    position: absolute; left: 735px; top: 10px; width: 353px; height: 406px;
    background: linear-gradient(180deg, rgba(58,31,26,.55) 0%, rgba(120,60,40,.6) 40%, rgba(194,122,82,.8) 100%);
  }
</style>
</head>
<body>
<div class="canvas">
  <section class="banner banner--first">
    <div class="product product--set" role="img" aria-label="Flat iron set with its box on a light blue background"></div>
    <div class="product product--spray" role="img" aria-label="Flat iron kit in an open box with accessories"></div>
    <svg class="frame" width="1088" height="416" aria-hidden="true">
      <path d="M397 93 H341 V253 H443 M634 253 H741 V93 H688" fill="none" stroke="#ffffff" stroke-width="2"/>
    </svg>
    <div class="title-black">BLACK</div>
    <div class="title-friday">FRIDAY</div>
    <div class="title-deal">Deal</div>
    <p class="offer">FREE HEAT PROTECTANT SPRAY<br>WITH ALL PURCHASES</p>
    <div class="shop-now">SHOP NOW</div>
    <div class="model" role="img" aria-label="Photo of a smiling model with a black bob haircut in a ribbed copper top"></div>
  </section>

  <section class="banner banner--second">
    <div class="product product--set" role="img" aria-label="Flat iron set with its box on a light blue background"></div>
    <div class="product product--spray" role="img" aria-label="Flat iron kit in an open box with accessories"></div>
    <svg class="frame" width="1088" height="416" aria-hidden="true">
      <path d="M397 93 H341 V253 H443 M634 253 H741 V93 H688" fill="none" stroke="#ffffff" stroke-width="2"/>
    </svg>
    <div class="title-black">BLACK</div>
    <div class="title-friday">FRIDAY</div>
    <div class="title-deal">Deal</div>
    <p class="offer">FREE HEAT PROTECTANT SPRAY<br>WITH ALL PURCHASES</p>
    <div class="shop-now">SHOP NOW</div>
    <div class="model" role="img" aria-label="Photo of a smiling model with a black bob haircut in a ribbed copper top"></div>
  </section>
</div>
</body>
</html>
```